Game, Voice & Dedicated Server Company Needs a Business Card Design

We need a new business card design, centered around our new logo (PSD provided below).

Designs that we do like:
https://pixelmarsh.net/item/corporate-business-card/5382017?s_rank=43 (needs to be made more eye catching)

Our main areas of business are:
- Dedicated Servers
- Game Servers
- Voice Servers
- Mitigation Security Specialists

Industry/Entity Type

Business

Contact Information for Business Card

On the card: (and anything else you would suggest)
- Staff member name
- Staff member position in company
- Staff member phone number
- Staff member email
- Other / Staff member plain circle
- Website link

Colors
9bcb3c
abd036

Requirements
Must have
• Design of Card:
• - Green (same green as the logo)
• - Business / Corporate design
• - Something a little different / abstract that shouts premium

```html
<!DOCTYPE html>
<html lang="en">
<head>
<meta charset="utf-8">
<title>Voltaric Servers – Business Card</title>
<link href="https://fonts.googleapis.com/css2?family=Open+Sans:wght@400;600;700&display=swap" rel="stylesheet">
<style>
  :root {
    --bg: #2e2f31;
    --card-dark: #2a2b2d;
    --green: #8cc63f;
    --grey-band: #8a8b8d;
    --white: #ffffff;
    --text-light: #d9d9d9;
  }
  html, body {
    margin: 0;
    width: 1200px;
    height: 900px;
    overflow: hidden;
    background: var(--bg);
    font-family: "Open Sans", Arial, sans-serif;
  }
  .canvas {
    position: relative;
    width: 1200px;
    height: 900px;
  }
  .card {
    position: absolute;
    top: 295px;
    width: 525px;
    height: 300px;
    border-radius: 26px;
    overflow: hidden;
    background: var(--card-dark);
    box-shadow: 0 18px 40px rgba(0,0,0,0.45);
  }
  .card--front { left: 50px; }
  .card--back { left: 625px; }
  .card__wave {
    position: absolute;
    inset: 0;
    width: 100%;
    height: 100%;
  }
  .wordmark {
    position: absolute;
    display: flex;
    align-items: center;
    gap: 12px;
    white-space: nowrap;
  }
  .wordmark__square {
    width: 34px;
    height: 34px;
    background: var(--green);
    flex: none;
  }
  .wordmark__name {
    color: var(--green);
    font-weight: 700;
    font-size: 27px;
    line-height: 1;
    letter-spacing: -0.5px;
    text-transform: uppercase;
  }
  .card--front .wordmark { left: 34px; top: 30px; }
  .card--front .wordmark__square { width: 26px; height: 26px; }
  .card--front .wordmark__name { font-size: 22px; }
  .card--back .wordmark { left: 50%; top: 50%; transform: translate(-50%, -50%); }
  .person {
    position: absolute;
    right: 36px;
    top: 72px;
    text-align: right;
  }
  .person__name {
    color: var(--green);
    font-weight: 700;
    font-size: 19px;
    margin: 0;
    line-height: 1.3;
  }
  .person__role {
    color: var(--text-light);
    font-size: 13px;
    margin: 2px 0 0;
  }
  .handle {
    position: absolute;
    left: 26px;
    top: 106px;
    display: flex;
    align-items: center;
    gap: 8px;
    color: var(--card-dark);
    font-size: 11px;
  }
  .handle__dot {
    width: 12px;
    height: 12px;
    border-radius: 50%;
    background: var(--card-dark);
  }
  .contacts {
    position: absolute;
    right: 30px;
    bottom: 22px;
    margin: 0;
    padding: 0;
    list-style: none;
  }
  .contacts__item {
    display: flex;
    justify-content: flex-end;
    align-items: center;
    gap: 8px;
    color: var(--white);
    font-size: 12.5px;
    line-height: 21px;
  }
  .contacts__icon {
    width: 16px;
    height: 16px;
    flex: none;
  }
</style>
</head>
<body>
<main class="canvas">

  <section class="card card--front" aria-label="Business card front">
    <svg class="card__wave" viewBox="0 0 525 300" preserveAspectRatio="none" aria-hidden="true">
      <path d="M0 76 C130 80 200 146 310 156 C410 165 470 152 525 138 L525 300 L0 300 Z" fill="#8a8b8d"/>
      <path d="M0 90 C130 94 200 160 310 170 C410 179 470 166 525 152 L525 300 L0 300 Z" fill="#8cc63f"/>
    </svg>

    <div class="wordmark">
      <span class="wordmark__square"></span>
      <span class="wordmark__name">Voltaric Servers</span>
    </div>

    <div class="person">
      <p class="person__name">Daniel Hayes</p>
      <p class="person__role">Managing Director</p>
    </div>

    <div class="handle">
      <span class="handle__dot"></span>
      <span>daniel_hayes</span>
    </div>

    <ul class="contacts">
      <li class="contacts__item">(555) 310-4720
        <svg class="contacts__icon" viewBox="0 0 16 16" aria-hidden="true"><circle cx="8" cy="8" r="7" fill="none" stroke="#2a2b2d" stroke-width="1.4"/><path d="M5.4 4.5l1.3 1.6-.7.9c.5 1 1.2 1.8 2.3 2.4l.9-.7 1.6 1.3-.8 1.2C7.6 11 5 8.5 4.3 5.3z" fill="#2a2b2d"/></svg>
      </li>
      <li class="contacts__item">(555) 310-4720
        <svg class="contacts__icon" viewBox="0 0 16 16" aria-hidden="true"><circle cx="8" cy="8" r="7" fill="none" stroke="#2a2b2d" stroke-width="1.4"/><rect x="5.5" y="4" width="5" height="8" rx="1" fill="none" stroke="#2a2b2d" stroke-width="1.2"/></svg>
      </li>
      <li class="contacts__item">info@voltaricservers.com
        <svg class="contacts__icon" viewBox="0 0 16 16" aria-hidden="true"><circle cx="8" cy="8" r="7" fill="none" stroke="#2a2b2d" stroke-width="1.4"/><rect x="4.3" y="5.3" width="7.4" height="5.4" fill="none" stroke="#2a2b2d" stroke-width="1.1"/><path d="M4.3 5.3L8 8.4l3.7-3.1" fill="none" stroke="#2a2b2d" stroke-width="1.1"/></svg>
      </li>
      <li class="contacts__item">www.voltaricservers.com
        <svg class="contacts__icon" viewBox="0 0 16 16" aria-hidden="true"><circle cx="8" cy="8" r="7" fill="none" stroke="#2a2b2d" stroke-width="1.4"/><circle cx="8" cy="8" r="4" fill="none" stroke="#2a2b2d" stroke-width="1.1"/><path d="M4 8h8M8 4c-1.6 2.4-1.6 5.6 0 8M8 4c1.6 2.4 1.6 5.6 0 8" fill="none" stroke="#2a2b2d" stroke-width="1"/></svg>
      </li>
    </ul>
  </section>

  <section class="card card--back" aria-label="Business card back">
    <div class="wordmark">
      <span class="wordmark__square"></span>
      <span class="wordmark__name">Voltaric Servers</span>
    </div>
  </section>

</main>
</body>
</html>
```